Business Card Ayurvedic Massage

I'm starting with my ayurvedic massage business and need a business card design. The design should be inline with my brand/logo as well as with the design of my website (www.lumo-thara.ch).
Front: logo and text "Ayurvedische Massagen"
back: name and adress (see details https://www.lumo-thara.ch/kontakt.html)

```html
<!DOCTYPE html>
<html lang="de">
<head>
<meta charset="utf-8">
<title>lumo-thara – Visitenkarte</title>
<link href="https://fonts.googleapis.com/css2?family=Source+Sans+3:wght@400;600;700&display=swap" rel="stylesheet">
<style>
  :root {
    --stage: #232323;
    --maroon: #7a0f1c;
    --red-dark: #6e0a10;
    --red: #a4121a;
    --gold: #d9a437;
    --gold-light: #f3d36b;
    --gold-deep: #b9801f;
    --ink: #3a3a3a;
    --paper: #ffffff;
  }
  * { margin: 0; padding: 0; box-sizing: border-box; }
  html, body { width: 1200px; height: 892px; overflow: hidden; }
  body {
    background: var(--stage);
    font-family: "Source Sans 3", "Myriad Pro", sans-serif;
    position: relative;
  }
  .card {
    position: absolute;
    left: 280px;
    width: 640px;
    height: 366px;
    overflow: hidden;
    box-shadow: 0 10px 30px rgba(0,0,0,.5);
  }
  /* Front */
  .card--front { top: 60px; }
  .front-ground {
    position: absolute; inset: 0;
    background: radial-gradient(ellipse at 50% 40%, var(--red) 0%, var(--red-dark) 100%);
  }
  .front-brand {
    position: absolute; left: 0; right: 0; top: 112px;
    text-align: center;
    color: var(--gold);
    font-weight: 700;
    font-size: 54px;
    line-height: 60px;
    letter-spacing: 1px;
  }
  .front-brand .mark-dot {
    display: inline-block; width: 18px; height: 18px; border-radius: 50%;
    background: var(--gold); margin-right: 14px; vertical-align: middle;
  }
  .front-tagline {
    position: absolute; left: 0; right: 0; top: 190px;
    text-align: center;
    color: var(--gold-light);
    font-weight: 400;
    font-size: 22px;
    line-height: 26px;
    letter-spacing: 2px;
  }
  .front-url {
    position: absolute; left: 0; right: 0; top: 268px;
    text-align: center;
    color: var(--gold);
    font-size: 17px;
    letter-spacing: 6px;
  }
  /* Back */
  .card--back { top: 466px; background: var(--paper); }
  .back-brand {
    position: absolute; right: 40px; top: 38px;
    color: var(--maroon);
    font-weight: 700;
    font-size: 40px;
    display: flex; align-items: center; gap: 12px;
  }
  .back-brand .mark-dot {
    width: 16px; height: 16px; border-radius: 50%; background: var(--gold);
  }
  .rule-top {
    position: absolute; left: 320px; right: 40px; top: 130px;
    height: 1.5px; background: var(--maroon);
  }
  .address {
    position: absolute; right: 40px; top: 140px;
    text-align: right; color: var(--ink);
    font-size: 17px; line-height: 22px; font-style: normal;
  }
  .person { position: absolute; left: 40px; top: 210px; }
  .person-name {
    color: var(--maroon); font-weight: 700; font-size: 26px; line-height: 28px;
  }
  .person-role {
    color: var(--gold-deep); font-size: 17px; letter-spacing: .5px;
  }
  .rule-bottom {
    position: absolute; left: 40px; width: 280px; top: 268px;
    height: 1.5px; background: var(--maroon);
  }
  .contacts {
    position: absolute; left: 40px; top: 276px;
    list-style: none; color: var(--ink); font-size: 17px; line-height: 20px;
  }
  .contacts li { display: flex; align-items: center; gap: 10px; }
  .contacts .note { font-size: 12px; margin-left: 4px; }
  .contacts svg { width: 14px; height: 14px; fill: var(--maroon); flex: none; }
  .band-gold {
    position: absolute; left: 0; bottom: 0; width: 480px; height: 16px;
    background: linear-gradient(90deg, var(--gold-deep), var(--gold-light) 60%, var(--gold));
  }
  .band-maroon {
    position: absolute; left: 484px; right: 0; bottom: 0; height: 22px;
    background: var(--maroon);
  }
</style>
</head>
<body>
  <section class="card card--front">
    <div class="front-ground" role="img" aria-label="Tiefroter Hintergrund mit dezentem Ornamentmuster"></div>
    <div class="front-brand"><span class="mark-dot"></span>lumo-thara</div>
    <div class="front-tagline">Ayurvedische Massagen</div>
    <div class="front-url">WWW.LUMO-THARA.CH</div>
  </section>

  <section class="card card--back">
    <div class="back-brand"><span class="mark-dot"></span>lumo-thara</div>
    <div class="rule-top"></div>
    <address class="address">
      Mira Keller, lumo-thara<br>
      Lindenweg 14<br>
      8855 Wangen (SZ)
    </address>

    <div class="person">
      <div class="person-name">ANNA MEIER</div>
      <div class="person-role">PRESIDENT</div>
    </div>
    <div class="rule-bottom"></div>
    <ul class="contacts">
      <li>
        <svg viewBox="0 0 24 24"><path d="M6.6 10.8a15 15 0 0 0 6.6 6.6l2.2-2.2a1 1 0 0 1 1-.25 11.4 11.4 0 0 0 3.6.57 1 1 0 0 1 1 1V20a1 1 0 0 1-1 1A17 17 0 0 1 3 4a1 1 0 0 1 1-1h3.5a1 1 0 0 1 1 1c0 1.25.2 2.45.57 3.57a1 1 0 0 1-.25 1z"/></svg>
        <span>+41 77 308 64 21<span class="note">(Bitte keine Werbung)</span></span>
      </li>
      <li>
        <svg viewBox="0 0 24 24"><path d="M2 5h20v14H2z M2 5l10 8 10-8" stroke="#fff" stroke-width="1.5"/></svg>
        <span>info@lumo-thara.ch</span>
      </li>
      <li>
        <svg viewBox="0 0 24 24"><circle cx="12" cy="12" r="10"/></svg>
        <span>www.lumo-thara.ch</span>
      </li>
    </ul>
    <div class="band-gold"></div>
    <div class="band-maroon"></div>
  </section>
</body>
</html>
```